Business needs Office Posters Designed

I need a office poster designed to put on a 2 feet x 3 feet space:
My Employee is Better Than Me.
- to signify the importance of listening to your employees, because they know better, more experienced in their respective fields.

Target Market(s)

employees

Industry/Entity Type

Healthcare

```html
<!DOCTYPE html>
<html lang="en">
<head>
<meta charset="UTF-8">
<title>My Employee is Better Than Me</title>
<link rel="stylesheet" href="https://fonts.googleapis.com/css2?family=Arimo:wght@400;700&display=swap">
<style>
  :root {
    --poster-teal: #017a94;
    --poster-ink: #ffffff;
  }
  html, body {
    margin: 0;
    padding: 0;
    overflow: hidden;
  }
  .poster {
    position: relative;
    width: 800px;
    height: 1200px;
    background: var(--poster-teal);
    color: var(--poster-ink);
    font-family: "Arimo", Helvetica, Arial, sans-serif;
    overflow: hidden;
  }
  .poster__headline {
    position: absolute;
    left: 76px;
    top: 161px;
    margin: 0;
    font-size: 148px;
    font-weight: 400;
    line-height: 229px;
    letter-spacing: -2px;
  }
  .poster__headline-line {
    display: block;
    white-space: nowrap;
  }
  .poster__emphasis {
    font-weight: 700;
  }
  .poster__tail {
    position: absolute;
    right: 42px;
    top: 1104px;
    margin: 0;
    font-size: 49px;
    font-weight: 400;
    line-height: 1;
    white-space: nowrap;
  }
</style>
</head>
<body>
  <main class="poster">
    <h1 class="poster__headline">
      <span class="poster__headline-line">My</span>
      <span class="poster__headline-line">Employee</span>
      <span class="poster__headline-line">is <strong class="poster__emphasis">Better</strong></span>
    </h1>
    <p class="poster__tail">Than Me</p>
  </main>
</body>
</html>
```